Business card design needed

I need a business card design for a dog walking, dog minding and dog training business. Please refer to my website for the basic company colours and fonts I'm after. Planning on a double sided card, so all information doesn't need to be on the 'front' side.
Cheers

Industry/Entity Type

Dog Training

Contact Information for Business Card

Meadow Paws - happy hounds
Rua 0498307164
meadowpawsdemo.com.au
-walking
-holiday stays
-onsite care
-training and behavioural consultations

```html
<!DOCTYPE html>
<html lang="en">
<head>
<meta charset="utf-8">
<title>Meadow Paws business cards</title>
<link rel="stylesheet" href="https://fonts.googleapis.com/css2?family=Kreon:wght@400;700&display=swap">
<style>
  :root {
    --orange: #e05a35;
    --charcoal: #2b2a29;
    --charcoal-deep: #1f1e1d;
    --white: #ffffff;
    --ink: #1c1c1c;
    --silhouette-dark: #4a4846;
    --silhouette-light: #e3e3e3;
    --coat-tan: #c47a45;
    --coat-light: #f1e7dc;
    --page: #ffffff;
  }
  * { box-sizing: border-box; margin: 0; padding: 0; }
  html, body {
    width: 955px;
    height: 1200px;
    overflow: hidden;
    background: var(--page);
    font-family: "Kreon", Georgia, serif;
  }
  .canvas { position: relative; width: 955px; height: 1200px; }

  .card {
    position: absolute;
    left: 18px;
    width: 918px;
    overflow: hidden;
  }
  .card--front {
    top: 18px;
    height: 528px;
    background: radial-gradient(ellipse at 40% 40%, var(--charcoal) 0%, var(--charcoal-deep) 100%);
  }
  .card--back {
    top: 636px;
    height: 535px;
    background: var(--white);
    border: 2px solid var(--ink);
  }

  .dog-silhouette { position: absolute; z-index: 0; border-radius: 40% 40% 8px 8px; }
  .card--front .dog-silhouette { background: var(--silhouette-dark); opacity: 0.5; }
  .card--back .dog-silhouette { background: var(--silhouette-light); }
  .card--front .dog-silhouette--hound { left: 55px; top: 362px; width: 190px; height: 88px; }
  .card--front .dog-silhouette--shepherd { left: 690px; top: 275px; width: 180px; height: 175px; }
  .card--back .dog-silhouette--hound { left: 36px; top: 362px; width: 175px; height: 145px; }
  .card--back .dog-silhouette--shepherd { left: 279px; top: 362px; width: 200px; height: 145px; }

  .brand-name, .tagline, .contact { position: absolute; z-index: 1; left: 40px; }
  .brand-name {
    top: 44px;
    font-size: 76px;
    font-weight: 700;
    line-height: 1;
    color: var(--orange);
    letter-spacing: 1px;
  }
  .tagline {
    top: 185px;
    font-size: 31px;
    font-weight: 400;
    line-height: 40px;
  }
  .contact {
    top: 229px;
    font-size: 40px;
    font-weight: 700;
    line-height: 57px;
    color: var(--orange);
  }
  .card--front .tagline { color: var(--white); }
  .card--back .tagline { color: var(--ink); }

  .services-band {
    position: absolute;
    z-index: 1;
    left: 0;
    bottom: 0;
    width: 100%;
    height: 74px;
    background: var(--orange);
    color: var(--white);
    font-size: 29px;
    line-height: 74px;
    padding-left: 30px;
  }

  .accent-strip {
    position: absolute;
    left: 0;
    top: 0;
    width: 100%;
    height: 10px;
    background: var(--orange);
  }

  .puppy-photo {
    position: absolute;
    left: 505px;
    top: 40px;
    width: 413px;
    height: 495px;
    background: radial-gradient(ellipse at 50% 45%, var(--coat-light) 0%, var(--coat-tan) 55%, var(--white) 100%);
  }
</style>
</head>
<body>
<main class="canvas">

  <section class="card card--front">
    <div class="dog-silhouette dog-silhouette--hound" role="img" aria-label="Faint silhouette of a hound dog"></div>
    <div class="dog-silhouette dog-silhouette--shepherd" role="img" aria-label="Faint silhouette of a shepherd dog"></div>
    <div class="brand-name">Meadow Paws</div>
    <p class="tagline">Happy hounds</p>
    <p class="contact">Rua 0498307164<br>meadowpawsdemo.com.au</p>
    <p class="services-band">stays, onsite care, training and behavioural consultations</p>
  </section>

  <section class="card card--back">
    <div class="accent-strip"></div>
    <div class="dog-silhouette dog-silhouette--hound" role="img" aria-label="Light grey silhouette of a hound dog"></div>
    <div class="dog-silhouette dog-silhouette--shepherd" role="img" aria-label="Light grey silhouette of a shepherd dog"></div>
    <div class="brand-name">Meadow Paws</div>
    <p class="tagline">Happy hounds</p>
    <p class="contact">Rua 0498307164<br>meadowpawsdemo.com.au</p>
    <div class="puppy-photo" role="img" aria-label="Photo of a tan and white puppy looking at the viewer"></div>
  </section>

</main>
</body>
</html>
```